Creative flyer for small business IT services

We are an IT services company based in Western Australia. We're looking to expand our market share amongst small businesses and need a brochure/flyer designed to give them a good overview of why we can help them. The design and layout should be consistent with an existing company profile brochure (included) but please be creative. A comprehensive brief with copy and a rough layout is included.

Small Business

```html
<!DOCTYPE html>
<html lang="en">
<head>
<meta charset="utf-8">
<title>Brightpath IT – Small Business Flyer</title>
<link href="https://fonts.googleapis.com/css2?family=Open+Sans:ital,wght@0,300;0,400;0,600;0,700;1,400;1,600&family=Ubuntu:wght@700&display=swap" rel="stylesheet">
<style>
:root{
  --red:#a01c21;
  --red-dark:#8e171b;
  --grey-panel:#e8e8e8;
  --ink:#3b3b3b;
  --ink-soft:#555;
  --white:#fff;
}
*{box-sizing:border-box;margin:0;padding:0}
html,body{width:933px;height:1200px;overflow:hidden;background:var(--white)}
body{font-family:"Open Sans",Arial,sans-serif;color:var(--ink)}
.flyer{position:relative;width:933px;height:1200px;background:var(--white)}
.abs{position:absolute}

.header{left:20px;top:16px;width:896px;height:194px;background:var(--red);color:var(--white)}
.header-corner{left:20px;top:209px}
.headline{left:39px;top:25px;font-family:"Ubuntu","Open Sans",sans-serif;font-weight:700;font-size:41px;line-height:52px;letter-spacing:-.5px;color:var(--white)}
.header-rule{left:39px;top:134px;width:601px;height:1px;background:rgba(255,255,255,.85)}
.tagline{left:39px;top:143px;font-size:38px;font-weight:300;letter-spacing:-1px;color:var(--white);white-space:nowrap}
.tagline strong{font-weight:700}
.brand-tile{left:752px;top:36px;width:141px;height:126px;background:var(--white)}
.brand-name{left:730px;top:163px;width:186px;text-align:center;font-size:24px;font-weight:400;color:var(--white)}

.hero-image{left:20px;top:218px;width:896px;height:169px;background:linear-gradient(180deg,#ffffff 0%,#ffffff 45%,#e4eed3 70%,#7a5a3f 88%,#5b3f2a 100%)}

.intro-title{left:20px;top:398px;font-size:34px;font-weight:300;line-height:40px;color:var(--ink)}
.accent{color:var(--red)}
.intro-flag{left:424px;top:405px}
.intro-panel{left:20px;top:493px;width:611px;height:116px;background:var(--grey-panel);padding:8px 8px}
.intro-panel p{font-size:15.5px;font-weight:300;line-height:21px;color:var(--ink)}
.intro-panel .lead{font-size:23px;line-height:30px;margin-top:7px}

.audit{left:646px;top:405px;width:270px;height:131px;background:var(--red);color:var(--white);padding:9px 8px;font-size:14px;line-height:17.5px;font-weight:400}

.testimonials{left:646px;top:551px;width:270px;height:267px;background:var(--red);color:var(--white);padding:8px 8px}
.testimonials .intro{font-size:14.5px;line-height:18px}
.quote{position:relative;background:var(--white);color:#444;font-style:italic;font-size:9.6px;line-height:12px;padding:5px 8px 6px;margin-top:8px;width:251px}
.quote::after{content:"";position:absolute;left:12px;bottom:-11px;border-left:12px solid var(--white);border-bottom:11px solid transparent}
.quote-by{font-size:10.5px;font-weight:700;font-style:italic;text-align:right;margin-top:3px;padding-right:2px}

.why-flag{left:20px;top:634px}
.why-title{right:302px;top:632px;font-size:34px;font-weight:300;line-height:39px;text-align:right;color:var(--ink);white-space:nowrap}
.why-panel{left:20px;top:717px;width:611px;height:101px;background:var(--grey-panel);padding:8px 8px}
.why-list{list-style:none}
.why-list li{display:flex;align-items:center;gap:6px;font-size:17px;font-weight:300;line-height:21.5px;color:var(--ink)}

.service{top:841px;width:283px}
.service-head{position:relative;height:42px}
.service-head svg{position:absolute;left:0;top:0}
.service-title{position:absolute;left:9px;top:10px;font-size:16px;font-weight:600;color:var(--white)}
.service-body{margin-top:9px;height:103px;background:var(--grey-panel);padding:6px 7px;font-size:8.4px;line-height:10.6px;color:var(--ink-soft)}

.partners-title{left:20px;top:1010px;font-size:14.5px;font-weight:600;color:var(--ink)}
.partners-text{left:20px;top:1043px;width:450px;font-size:11.6px;line-height:14.6px;color:var(--ink)}
.badge{background:#d9d9d9}
.badge-wide{left:596px;top:1020px;width:170px;height:24px;background:#cfcfcf}
.badge-dark{left:593px;top:1056px;width:124px;height:48px;background:#1f3e6e}
.badge-light{left:727px;top:1058px;width:53px;height:46px;background:#eef3f7;border:1px solid #cdd7df}
.badge-card{left:790px;top:1019px;width:126px;height:86px;background:linear-gradient(180deg,#f4f4f4,#d6d6d6);border-radius:4px;box-shadow:0 1px 3px rgba(0,0,0,.35)}
.badge-card .stripe{position:absolute;left:12px;top:23px;width:107px;height:14px;background:#d1121a}
.badge-card .dot{position:absolute;left:61px;top:55px;width:16px;height:16px;border-radius:50%;background:#d1121a}

.closing{left:20px;top:1112px;font-size:15.2px;color:var(--ink);white-space:nowrap}

.footer{left:20px;top:1146px;width:896px;height:40px}
.footer-mark{left:20px;top:1146px;width:32px;height:32px;background:var(--red)}
.footer-brand{left:60px;top:1151px;font-size:17px;font-weight:400;color:var(--ink)}
.footer-sep{top:1142px;width:1px;height:44px;background:#777}
.footer-address{left:195px;top:1150px;width:185px;text-align:center;font-size:9.6px;line-height:12px}
.footer-contact{left:392px;top:1150px;width:212px;text-align:center;font-size:9.6px;line-height:12px}
.footer-contact b{font-weight:700}
.footer-phone{left:636px;top:1150px;font-size:18px;font-weight:700;color:var(--ink)}
.footer-flag{left:766px;top:1146px}
</style>
</head>
<body>
<div class="flyer">

  <div class="abs header"></div>
  <svg class="abs header-corner" width="75" height="71" viewBox="0 0 75 71"><polygon points="0,0 74,0 0,70" fill="var(--red)"/></svg>
  <div class="abs headline">Small Business.<br>Big Ideas.</div>
  <div class="abs header-rule"></div>
  <div class="abs tagline">We’ll help <strong>your business</strong> grow…</div>
  <div class="abs brand-tile"></div>
  <div class="abs brand-name">Brightpath IT</div>

  <div class="abs hero-image" role="img" aria-label="Row of seedlings sprouting from mounds of soil, growing larger from left to right"></div>

  <div class="abs intro-title">We help small businesses<br><span class="accent">get ahead</span> of the pack.</div>
  <svg class="abs intro-flag" width="207" height="64" viewBox="0 0 207 64"><polygon points="0,64 72,0 207,0 207,64" fill="var(--red)"/></svg>
  <div class="abs intro-panel">
    <p>You’ve always got more to do. In a small business, the last thing you need is another hat to wear. You shouldn’t need to become a computer engineer to keep your business running smoothly. Say goodbye to IT headaches…</p>
    <p class="lead">Our job is to make <span class="accent">your life</span> easier.</p>
  </div>

  <div class="abs audit">It helps to know where you stand. Get a clearer picture of your IT systems with our obligation-free IT audit and consultation. Contact us today and we’ll provide you with expert insights into how your business can benefit from today’s amazing technology.</div>

  <div class="abs testimonials">
    <p class="intro">Don’t just take our word for it! Here’s what some satisfied customers have to say about Brightpath IT:</p>
    <div class="quote">“We are pleased to have Brightpath IT as part of our team. I recommend Brightpath IT for any business seeking a trustworthy, reliable and effective IT service provider.”</div>
    <p class="quote-by">Lena Marsh, Harbour Imaging</p>
    <div class="quote">“Brightpath IT’s expertise has allowed us to test, analyse and improve the reliability and performance of our application, further improving the health and financial status of our business.”</div>
    <p class="quote-by">Tom Rydell, Gradeline Pty Ltd</p>
  </div>

  <svg class="abs why-flag" width="257" height="63" viewBox="0 0 257 63"><polygon points="0,0 190,0 256,63 0,63" fill="var(--red)"/></svg>
  <div class="abs why-title">Here’s why <span class="accent">people love</span><br>Brightpath IT…</div>
  <div class="abs why-panel">
    <ul class="why-list">
      <li><svg width="16" height="16" viewBox="0 0 16 16"><path d="M1 9 L6 14 L15 1" fill="none" stroke="var(--red)" stroke-width="2.6"/></svg>We’re small business IT experts</li>
      <li><svg width="16" height="16" viewBox="0 0 16 16"><path d="M1 9 L6 14 L15 1" fill="none" stroke="var(--red)" stroke-width="2.6"/></svg>We speak plain English and won’t waste your time</li>
      <li><svg width="16" height="16" viewBox="0 0 16 16"><path d="M1 9 L6 14 L15 1" fill="none" stroke="var(--red)" stroke-width="2.6"/></svg>We care about our relationships</li>
      <li><svg width="16" height="16" viewBox="0 0 16 16"><path d="M1 9 L6 14 L15 1" fill="none" stroke="var(--red)" stroke-width="2.6"/></svg>We worry about IT so you don’t have to</li>
    </ul>
  </div>

  <section class="abs service" style="left:20px">
    <div class="service-head">
      <svg width="283" height="42" viewBox="0 0 283 42">
        <polygon points="0,0 190,0 232,42 0,42" fill="var(--red)"/>
        <g fill="#333"><circle cx="258" cy="18" r="12"/><rect x="242" y="32" width="32" height="10" rx="4"/></g>
        <path d="M244 20 a14 14 0 0 1 28 0" fill="none" stroke="#333" stroke-width="3"/>
      </svg>
      <span class="service-title">Support Services</span>
    </div>
    <p class="service-body">Say goodbye to IT interruptions, slow services, confusing jargon and inexplicable errors. We have solutions to your IT problems, and packages to suit every budget. We can even come to your workplace. If you run into a problem or need something done, just contact our Service Desk. Whether you have a single computer or a big team with complex requirements, our expert team can assist. We’ll give you an entire IT department for a fraction of the cost.</p>
  </section>

  <section class="abs service" style="left:326px">
    <div class="service-head">
      <svg width="283" height="42" viewBox="0 0 283 42">
        <polygon points="0,0 186,0 228,42 0,42" fill="var(--red)"/>
        <rect x="241" y="0" width="42" height="42" fill="#333"/>
        <path d="M244 24 H252 L256 12 L261 34 L266 6 L271 28 L274 22 H281" fill="none" stroke="#fff" stroke-width="2.4"/>
      </svg>
      <span class="service-title">Monitoring &amp; Backup</span>
    </div>
    <p class="service-body">Most of us insure our cars and homes, yet small businesses often don’t protect themselves from the kind of disaster that strikes every day. Could your business recover from the complete loss of every electronic file - financial records, legal documents, customer information, intellectual property, archives, emails and more? Our Monitor &amp; Protect solutions keep you safe from physical threats like theft, fire and floods, but also from electronic threats like viruses and hackers. Best of all - it happens automatically, so you can relax.</p>
  </section>

  <section class="abs service" style="left:631px;width:285px">
    <div class="service-head">
      <svg width="285" height="42" viewBox="0 0 285 42">
        <polygon points="0,0 190,0 232,42 0,42" fill="var(--red)"/>
        <rect x="240" y="0" width="30" height="36" rx="3" fill="#333"/>
        <circle cx="266" cy="30" r="12" fill="#fff" stroke="#333" stroke-width="3"/>
        <circle cx="266" cy="30" r="3" fill="#333"/>
      </svg>
      <span class="service-title">Hardware &amp; Software</span>
    </div>
    <p class="service-body">Every business needs the right tools for the job. We supply world class hardware and software products from Northwind, Halden, Corvex, Orchard, Lumana, Pixelon, Voltra and many more. Our strong partnerships and buying power mean we can save you money. From a single keyboard to an entire infrastructure, we always take the time to help you select the right products.</p>
  </section>

  <h2 class="abs partners-title">World Class Partnerships…</h2>
  <p class="abs partners-text">We proudly work with a range of industry leaders to ensure your business is powered by the best of today’s technology. With major partners including Northwind, Corvex, Lumana, Stratos and Veyra, you can be confident that our solutions are built on a strong foundation.</p>

  <div class="abs badge-wide" aria-label="Partner badge"></div>
  <div class="abs badge-dark" aria-label="Partner badge"></div>
  <div class="abs badge-light" aria-label="Partner badge"></div>
  <div class="abs badge-card" aria-label="Partner badge"><span class="stripe"></span><span class="dot"></span></div>

  <p class="abs closing">Our valued customers are already enjoying the benefits of partnering with Brightpath IT. <span class="accent">Join them by contacting us today:</span></p>

  <div class="abs footer-mark"></div>
  <div class="abs footer-brand">Brightpath IT</div>
  <div class="abs footer-sep" style="left:186px"></div>
  <div class="abs footer-address">Level 9, 120 Kestrel Terrace<br>Perth WA 6000</div>
  <div class="abs footer-sep" style="left:393px"></div>
  <div class="abs footer-contact">sales@brightpathit.example<br><b>www.brightpathit.example</b></div>
  <div class="abs footer-sep" style="left:611px"></div>
  <div class="abs footer-phone">1300 555 019</div>
  <svg class="abs footer-flag" width="150" height="40" viewBox="0 0 150 40"><polygon points="0,40 42,0 150,0 150,40" fill="var(--red)"/></svg>

</div>
</body>
</html>
```